Corporate Branded Documents - IT Provider - On-going work

Hi, I'm Tom a Director of Harbourline IT Care a UK Based IT & Telecoms support firm. We've been trading for 12 years now and feel its time for a lick of paint. We have a logo, website etc but would like someone to create some standard documents for us.

- A PDF Proposal Template - We currently don't send our customers proposals as we have nothing that looks good.
- A Quote Template PDF - Example Attached
- A Order Template PDF - Example Attached
- A Invoice Template PDF - Example Attached
- A Generic Document PDF - Something we can use for customer application forms, NDA Agreements, Terms & Conditions etc

Our website can be found at www.harbourlineitcare.co.uk - here you'll get a feel for our branding. I've also attached 2 example documents - as well as our currently used documents. Hopefully you guys can see why it needs improving.

We'd also like to work with someone long term, these documents are a start but we'd like to make sure all the work we do looks and feels as smart as possible, so there is plenty of additional work available.

None of these templates need to be Print ready, 99% of the time it will be viewed digitally, so high resolution designs are best

Thanks,

Tom

Target Market(s)

Corporate & Educational Customers

Industry/Entity Type

It Support

Font styles to use
Sans Serif

Colors
ec1f27
0692cd
ffffff

```html
<!DOCTYPE html>
<html lang="en">
<head>
<meta charset="utf-8">
<title>Harbourline IT Care – IT &amp; Telecoms Support Proposal</title>
<link rel="stylesheet" href="https://fonts.googleapis.com/css2?family=Open+Sans:wght@300;400;600;700;800&display=swap">
<style>
:root{
  --red:#ec1f27;
  --blue:#0692cd;
  --blue-deep:#0a6fb3;
  --teal:#1b7f9c;
  --white:#ffffff;
  --ink:#222222;
  --body:#333333;
  --tag:#d9d9d9;
  --tile:#ececec;
  --stage-dark:#2b2b2b;
  --stage-light:#cfcfcf;
  --footer:#ededed;
}
*{box-sizing:border-box;margin:0;padding:0}
html,body{width:1200px;height:2568px;overflow:hidden}
body{font-family:"Open Sans",Arial,sans-serif;background:var(--stage-light);position:relative;color:var(--body)}
.stage-top{position:absolute;left:0;top:0;width:1200px;height:1019px;background:radial-gradient(ellipse at 50% 40%,#4a4a4a 0%,var(--stage-dark) 75%)}
.page-label{position:absolute;width:491px;text-align:center;font-weight:600;font-size:22px;letter-spacing:.5px;color:var(--ink)}
.page{position:absolute;width:491px;height:688px;background:var(--white);box-shadow:0 3px 10px rgba(0,0,0,.25);overflow:hidden}
.page > *{position:absolute}
.page--hero{transform:scale(1.3);transform-origin:0 0;box-shadow:0 20px 50px rgba(0,0,0,.6)}
.page--blue{background:linear-gradient(135deg,var(--blue-deep) 0%,var(--blue) 100%)}

/* cover */
.cover-photo{left:22px;top:24px;width:447px;height:424px;background:radial-gradient(ellipse at 55% 45%,#3a6fb0 0%,#1b2e55 45%,#0d1424 100%)}
.cover-tag{left:0;top:60px;width:298px;height:88px;background:var(--red);color:var(--white);padding:12px 0 0 38px}
.cover-tag__kicker{font-size:19px;font-weight:400;display:block;line-height:1}
.cover-tag__title{font-size:42px;font-weight:800;display:block;line-height:1.05}
.cover-rule{left:22px;top:450px;width:392px;height:7px;background:var(--red)}
.cover-square{left:420px;top:440px;width:48px;height:48px;background:var(--red)}
.cover-brand{left:0;top:520px;width:491px;display:flex;justify-content:center;align-items:center;gap:14px}
.cover-brand__mark{width:46px;height:46px;background:var(--red);flex:none}
.cover-brand__name{font-size:38px;font-weight:700;color:var(--teal);line-height:1}

/* footer */
.footer{left:0;top:620px;width:491px;height:68px;background:var(--footer)}
.footer__contacts{position:absolute;left:0;top:12px;width:491px;display:flex;justify-content:space-around;padding:0 40px}
.footer__item{display:flex;align-items:center;gap:6px;font-size:11px;font-weight:600;color:var(--ink)}
.footer__item svg{width:14px;height:14px}
.footer__pattern{position:absolute;left:0;top:40px;width:491px;height:28px;background:linear-gradient(180deg,#e2e6e8 0%,#9fc9d3 60%,#3d98ac 100%)}

/* inner headers */
.doc-tag{left:24px;top:26px;width:164px;height:18px;background:var(--tag);font-size:8px;font-weight:600;color:#555;padding:3px 0 0 10px;letter-spacing:.3px}
.page--blue .doc-tag{background:var(--white);color:var(--blue-deep)}
.doc-brand{left:318px;top:24px;display:flex;align-items:center;gap:6px}
.doc-brand__mark{width:16px;height:16px;background:var(--red)}
.doc-brand__name{font-size:13px;font-weight:700;color:var(--teal)}
.page--blue .doc-brand__mark{background:var(--white)}
.page--blue .doc-brand__name{color:var(--white)}
.section-title{left:24px;top:86px;display:flex;align-items:center;gap:14px}
.section-title__mark{width:52px;height:52px;background:var(--red)}
.page--blue .section-title__mark{background:var(--white)}
.section-title__kicker{display:block;font-size:17px;font-weight:400;color:var(--red);line-height:1.1}
.section-title__main{display:block;font-weight:700;font-size:40px;color:var(--ink);line-height:1}
.page--blue .section-title__kicker,.page--blue .section-title__main{color:var(--white)}
.section-rule{left:24px;top:164px;width:443px;height:2px;background:var(--red)}
.page--blue .section-rule{background:rgba(255,255,255,.55)}

/* about */
.about-photo{left:26px;top:180px;width:441px;height:175px;background:linear-gradient(120deg,#5a5e66 0%,#2e3137 55%,#1a1c20 100%)}
.about-copy{left:26px;top:376px;width:441px}
.about-block{margin-bottom:14px}
.about-block__head{display:flex;align-items:center;gap:6px;font-size:8.5px;font-weight:700;color:var(--ink)}
.about-block__head::before{content:"";width:7px;height:7px;background:var(--red)}
.about-block p{font-size:8.2px;line-height:1.38;text-align:justify;padding-left:13px;color:var(--body)}

/* summary */
.summary-list{left:36px;top:188px;width:420px}
.summary-item{display:flex;gap:14px;height:108px}
.summary-item__icon{width:64px;height:64px;background:var(--white);flex:none;display:flex;align-items:center;justify-content:center}
.summary-item__icon svg{width:40px;height:40px}
.summary-item h3{font-size:14px;font-weight:800;color:var(--white);line-height:1.2}
.summary-item p{font-size:8.2px;line-height:1.36;color:var(--white)}

/* services */
.services-intro{left:26px;top:180px;width:443px;height:171px;background:var(--blue);color:var(--white);padding:14px 16px}
.services-intro h3{font-size:9px;font-weight:700;margin-bottom:3px}
.services-intro p{font-size:8.2px;line-height:1.4;margin-bottom:8px}
.service-grid{left:26px;top:380px;width:443px;display:grid;grid-template-columns:repeat(4,103px);grid-auto-rows:106px;gap:8px 10px}
.service-tile{background:var(--tile);display:flex;flex-direction:column;align-items:center;justify-content:center;gap:8px}
.service-tile svg{width:46px;height:40px}
.service-tile span{font-size:7px;font-weight:700;color:#444;letter-spacing:.3px}
.service-tile--accent{background:var(--red)}
</style>
</head>
<body>

<div class="stage-top"></div>

<!-- hero cover -->
<section class="page page--hero" style="left:281px;top:62px" aria-label="Proposal cover">
  <div class="cover-photo" role="img" aria-label="Night city skyline with glowing network connection lines"></div>
  <div class="cover-tag"><span class="cover-tag__kicker">IT &amp; TELECOMS SUPPORT</span><span class="cover-tag__title">PROPOSAL</span></div>
  <div class="cover-rule"></div>
  <div class="cover-square"></div>
  <div class="cover-brand"><span class="cover-brand__mark"></span><span class="cover-brand__name">Harbourline IT Care</span></div>
  <footer class="footer">
    <div class="footer__contacts">
      <span class="footer__item"><svg viewBox="0 0 14 14"><circle cx="7" cy="7" r="7" fill="#0692cd"/><path d="M4.5 3.5l1.5 0 .6 2-1 .7a5 5 0 0 0 2.2 2.2l.7-1 2 .6v1.5c-3.6.3-6.3-2.4-6-6z" fill="#fff"/></svg>0113 496 0721</span>
      <span class="footer__item"><svg viewBox="0 0 14 14"><circle cx="7" cy="7" r="7" fill="#0692cd"/><rect x="5" y="3" width="4" height="8" rx="1" fill="#fff"/></svg>0871 496 0388</span>
      <span class="footer__item"><svg viewBox="0 0 14 14"><circle cx="7" cy="7" r="7" fill="#0692cd"/><circle cx="7" cy="7" r="3.5" fill="none" stroke="#fff"/><path d="M3.5 7h7M7 3.5v7" stroke="#fff" stroke-width=".8"/></svg>www.harbourlineitcare.co.uk</span>
    </div>
    <div class="footer__pattern" role="img" aria-label="Decorative geometric pattern band"></div>
  </footer>
</section>

<span class="page-label" style="left:108px;top:1040px">COVER PAGE</span>
<span class="page-label" style="left:613px;top:1040px">INNER PAGE 1</span>

<!-- cover page -->
<section class="page" style="left:108px;top:1084px" aria-label="Cover page">
  <div class="cover-photo" role="img" aria-label="Night city skyline with glowing network connection lines"></div>
  <div class="cover-tag"><span class="cover-tag__kicker">IT &amp; TELECOMS SUPPORT</span><span class="cover-tag__title">PROPOSAL</span></div>
  <div class="cover-rule"></div>
  <div class="cover-square"></div>
  <div class="cover-brand"><span class="cover-brand__mark"></span><span class="cover-brand__name">Harbourline IT Care</span></div>
  <footer class="footer">
    <div class="footer__contacts">
      <span class="footer__item"><svg viewBox="0 0 14 14"><circle cx="7" cy="7" r="7" fill="#0692cd"/><path d="M4.5 3.5l1.5 0 .6 2-1 .7a5 5 0 0 0 2.2 2.2l.7-1 2 .6v1.5c-3.6.3-6.3-2.4-6-6z" fill="#fff"/></svg>0113 496 0721</span>
      <span class="footer__item"><svg viewBox="0 0 14 14"><circle cx="7" cy="7" r="7" fill="#0692cd"/><rect x="5" y="3" width="4" height="8" rx="1" fill="#fff"/></svg>0871 496 0388</span>
      <span class="footer__item"><svg viewBox="0 0 14 14"><circle cx="7" cy="7" r="7" fill="#0692cd"/><circle cx="7" cy="7" r="3.5" fill="none" stroke="#fff"/><path d="M3.5 7h7M7 3.5v7" stroke="#fff" stroke-width=".8"/></svg>www.harbourlineitcare.co.uk</span>
    </div>
    <div class="footer__pattern" role="img" aria-label="Decorative geometric pattern band"></div>
  </footer>
</section>

<!-- inner page 1 -->
<section class="page" style="left:613px;top:1084px" aria-label="About our company">
  <div class="doc-tag">IT &amp; TELECOMS SUPPORT</div>
  <div class="doc-brand"><span class="doc-brand__mark"></span><span class="doc-brand__name">Harbourline IT Care</span></div>
  <div class="section-title"><span class="section-title__mark"></span><div><span class="section-title__kicker">ABOUT OUR</span><span class="section-title__main">COMPANY</span></div></div>
  <div class="section-rule"></div>
  <div class="about-photo" role="img" aria-label="Hands typing on a laptop keyboard in low light"></div>
  <div class="about-copy">
    <div class="about-block">
      <div class="about-block__head">THE IMPORTANCE OF HIRING A PROFESSIONAL IT SUPPORT PARTNER</div>
      <p>Lorem Ipsum is simply dummy text of the printing and typesetting industry. Lorem Ipsum has been the industry's standard dummy text ever since the 1500s, when an unknown printer took a galley of type and scrambled it to make a type specimen book. It has survived not only five centuries, but also the leap into electronic typesetting, remaining essentially unchanged. It was popularised in the 1960s with the release of transfer sheets containing Lorem Ipsum passages, and more recently with desktop publishing software like page layout software including versions of Lorem Ipsum.</p>
    </div>
    <div class="about-block">
      <div class="about-block__head">WHO WE ARE</div>
      <p>Lorem Ipsum is simply dummy text of the printing and typesetting industry. Lorem Ipsum has been the industry's standard dummy text ever since the 1500s, when an unknown printer took a galley of type and scrambled it to make a type specimen book. It has survived not only five centuries, but also the leap into electronic typesetting, remaining essentially unchanged. It was popularised in the 1960s with the release of transfer sheets containing Lorem Ipsum passages, and more recently with desktop publishing software like page layout software including versions of Lorem Ipsum.</p>
    </div>
  </div>
  <footer class="footer">
    <div class="footer__contacts">
      <span class="footer__item"><svg viewBox="0 0 14 14"><circle cx="7" cy="7" r="7" fill="#0692cd"/><path d="M4.5 3.5l1.5 0 .6 2-1 .7a5 5 0 0 0 2.2 2.2l.7-1 2 .6v1.5c-3.6.3-6.3-2.4-6-6z" fill="#fff"/></svg>0113 496 0721</span>
      <span class="footer__item"><svg viewBox="0 0 14 14"><circle cx="7" cy="7" r="7" fill="#0692cd"/><rect x="5" y="3" width="4" height="8" rx="1" fill="#fff"/></svg>0871 496 0388</span>
      <span class="footer__item"><svg viewBox="0 0 14 14"><circle cx="7" cy="7" r="7" fill="#0692cd"/><circle cx="7" cy="7" r="3.5" fill="none" stroke="#fff"/><path d="M3.5 7h7M7 3.5v7" stroke="#fff" stroke-width=".8"/></svg>www.harbourlineitcare.co.uk</span>
    </div>
    <div class="footer__pattern" role="img" aria-label="Decorative geometric pattern band"></div>
  </footer>
</section>

<!-- inner page 2 -->
<section class="page page--blue" style="left:108px;top:1798px" aria-label="Company summary">
  <div class="doc-tag">IT &amp; TELECOMS SUPPORT</div>
  <div class="doc-brand"><span class="doc-brand__mark"></span><span class="doc-brand__name">Harbourline IT Care</span></div>
  <div class="section-title"><span class="section-title__mark"></span><div><span class="section-title__kicker">COMPANY</span><span class="section-title__main">SUMMARY</span></div></div>
  <div class="section-rule"></div>
  <div class="summary-list">
    <div class="summary-item">
      <div class="summary-item__icon"><svg viewBox="0 0 40 40" fill="none" stroke="#ec1f27" stroke-width="2"><rect x="8" y="5" width="24" height="30" rx="2"/><path d="M13 13h14M13 20h14M13 27h9"/></svg></div>
      <div><h3>HEADING ONE</h3><p>Lorem Ipsum is simply dummy text of the printing and typesetting industry. Lorem Ipsum has been the industry's standard dummy text ever since the 1500s, when an unknown printer took a galley of type and scrambled it to make a type specimen book. It has survived not only five centuries, but also the leap into electronic typesetting, remaining essentially unchanged.</p></div>
    </div>
    <div class="summary-item">
      <div class="summary-item__icon"><svg viewBox="0 0 40 40" fill="none" stroke="#ec1f27" stroke-width="2"><path d="M6 8h20v14H14l-6 5v-5H6z"/><path d="M18 26h12l4 4v-4h2V14h-6"/></svg></div>
      <div><h3>HEADING TWO</h3><p>Lorem Ipsum is simply dummy text of the printing and typesetting industry. Lorem Ipsum has been the industry's standard dummy text ever since the 1500s, when an unknown printer took a galley of type and scrambled it to make a type specimen book. It has survived not only five centuries, but also the leap into electronic typesetting, remaining essentially unchanged.</p></div>
    </div>
    <div class="summary-item">
      <div class="summary-item__icon"><svg viewBox="0 0 40 40" fill="none" stroke="#ec1f27" stroke-width="2"><circle cx="20" cy="20" r="13"/><path d="M7 20h26M20 7c-6 7-6 19 0 26M20 7c6 7 6 19 0 26"/></svg></div>
      <div><h3>HEADING THREE</h3><p>Lorem Ipsum is simply dummy text of the printing and typesetting industry. Lorem Ipsum has been the industry's standard dummy text ever since the 1500s, when an unknown printer took a galley of type and scrambled it to make a type specimen book. It has survived not only five centuries, but also the leap into electronic typesetting, remaining essentially unchanged.</p></div>
    </div>
    <div class="summary-item">
      <div class="summary-item__icon"><svg viewBox="0 0 40 40" fill="none" stroke="#ec1f27" stroke-width="2"><rect x="9" y="10" width="22" height="15" rx="1"/><path d="M4 30h32"/></svg></div>
      <div><h3>HEADING FOUR</h3><p>Lorem Ipsum is simply dummy text of the printing and typesetting industry. Lorem Ipsum has been the industry's standard dummy text ever since the 1500s, when an unknown printer took a galley of type and scrambled it to make a type specimen book. It has survived not only five centuries, but also the leap into electronic typesetting, remaining essentially unchanged.</p></div>
    </div>
  </div>
  <footer class="footer">
    <div class="footer__contacts">
      <span class="footer__item"><svg viewBox="0 0 14 14"><circle cx="7" cy="7" r="7" fill="#0692cd"/><path d="M4.5 3.5l1.5 0 .6 2-1 .7a5 5 0 0 0 2.2 2.2l.7-1 2 .6v1.5c-3.6.3-6.3-2.4-6-6z" fill="#fff"/></svg>0113 496 0721</span>
      <span class="footer__item"><svg viewBox="0 0 14 14"><circle cx="7" cy="7" r="7" fill="#0692cd"/><rect x="5" y="3" width="4" height="8" rx="1" fill="#fff"/></svg>0871 496 0388</span>
      <span class="footer__item"><svg viewBox="0 0 14 14"><circle cx="7" cy="7" r="7" fill="#0692cd"/><circle cx="7" cy="7" r="3.5" fill="none" stroke="#fff"/><path d="M3.5 7h7M7 3.5v7" stroke="#fff" stroke-width=".8"/></svg>www.harbourlineitcare.co.uk</span>
    </div>
    <div class="footer__pattern" role="img" aria-label="Decorative geometric pattern band"></div>
  </footer>
</section>

<!-- inner page 3 -->
<section class="page" style="left:613px;top:1798px" aria-label="Our services">
  <div class="doc-tag">IT &amp; TELECOMS SUPPORT</div>
  <div class="doc-brand"><span class="doc-brand__mark"></span><span class="doc-brand__name">Harbourline IT Care</span></div>
  <div class="section-title"><span class="section-title__mark"></span><div><span class="section-title__kicker">OUR</span><span class="section-title__main">SERVICES</span></div></div>
  <div class="section-rule"></div>
  <div class="services-intro">
    <h3>HARBOURLINE IT CARE</h3>
    <p>Founded in 2006, Harbourline IT Care has one focus, to take away the burden of technology and allowing organisations to harness the creative and dynamic environment that a well managed ICT Infrastructure can provide. Our mission is to provide a sustainable network that is both efficient and stable for its users, cost effective and well planned. We have consistently pushed the boundaries, listened to our customers, focusing on the benefits to them, not us.</p>
    <p>We are user focused IT support company, understanding that even the smallest of requests are important and that we become the trusted IT support team of every customer we work with. Delivering a 360 degree service for our clients, we always look to improve on their experience by aligning our support service. We are user centric.</p>
  </div>
  <div class="service-grid">
    <div class="service-tile"><svg viewBox="0 0 46 40" fill="none" stroke="#0692cd" stroke-width="2.5"><rect x="9" y="8" width="28" height="19" rx="1"/><path d="M3 32h40"/></svg><span>IT SUPPORT</span></div>
    <div class="service-tile"><svg viewBox="0 0 46 40"><circle cx="23" cy="20" r="16" fill="#0692cd"/><path d="M14 14c4 0 5 4 9 3s2 6 6 6M28 10c-2 3 1 5 4 4" stroke="#fff" stroke-width="2" fill="none"/></svg><span>WEB SERVICES</span></div>
    <div class="service-tile"><svg viewBox="0 0 46 40"><path d="M16 18v-6a7 7 0 0 1 14 0v6" fill="none" stroke="#0692cd" stroke-width="3"/><rect x="12" y="18" width="22" height="18" rx="2" fill="#0692cd"/><circle cx="23" cy="26" r="2.5" fill="#fff"/></svg><span>ENDPOINT SECURITY</span></div>
    <div class="service-tile"><svg viewBox="0 0 46 40"><path d="M12 32a8 8 0 0 1 0-16 11 11 0 0 1 21-2 9 9 0 0 1 1 18z" fill="#0692cd"/><path d="M23 14v12M18 21l5 5 5-5" stroke="#fff" stroke-width="2.5" fill="none"/></svg><span>REMOTE BACKUP</span></div>
    <div class="service-tile"><svg viewBox="0 0 46 40"><path d="M3 20c10-14 30-14 40 0-10 14-30 14-40 0z" fill="#0692cd"/><circle cx="23" cy="20" r="7" fill="#fff"/><circle cx="23" cy="20" r="3.5" fill="#0692cd"/></svg><span>AUDIO VISUAL</span></div>
    <div class="service-tile"><svg viewBox="0 0 46 40"><path d="M7 30a16 16 0 1 1 32 0" fill="none" stroke="#0692cd" stroke-width="5"/><path d="M23 30l8-11" stroke="#0692cd" stroke-width="3"/><circle cx="23" cy="30" r="3" fill="#0692cd"/></svg><span>BROADBAND</span></div>
    <div class="service-tile"><svg viewBox="0 0 46 40"><rect x="15" y="4" width="16" height="18" rx="2" fill="#0692cd"/><path d="M19 9v6M23 9v6M27 9v6" stroke="#fff" stroke-width="1.6"/><path d="M23 22v14" stroke="#0692cd" stroke-width="4"/></svg><span>DATA CABLING</span></div>
    <div class="service-tile service-tile--accent"></div>
  </div>
  <footer class="footer">
    <div class="footer__contacts">
      <span class="footer__item"><svg viewBox="0 0 14 14"><circle cx="7" cy="7" r="7" fill="#0692cd"/><path d="M4.5 3.5l1.5 0 .6 2-1 .7a5 5 0 0 0 2.2 2.2l.7-1 2 .6v1.5c-3.6.3-6.3-2.4-6-6z" fill="#fff"/></svg>0113 496 0721</span>
      <span class="footer__item"><svg viewBox="0 0 14 14"><circle cx="7" cy="7" r="7" fill="#0692cd"/><rect x="5" y="3" width="4" height="8" rx="1" fill="#fff"/></svg>0871 496 0388</span>
      <span class="footer__item"><svg viewBox="0 0 14 14"><circle cx="7" cy="7" r="7" fill="#0692cd"/><circle cx="7" cy="7" r="3.5" fill="none" stroke="#fff"/><path d="M3.5 7h7M7 3.5v7" stroke="#fff" stroke-width=".8"/></svg>www.harbourlineitcare.co.uk</span>
    </div>
    <div class="footer__pattern" role="img" aria-label="Decorative geometric pattern band"></div>
  </footer>
</section>

<span class="page-label" style="left:108px;top:2510px">INNER PAGE 2</span>
<span class="page-label" style="left:613px;top:2510px">INNER PAGE 3</span>

</body>
</html>
```